Business Cards for a start up company

We are looking for a business card design for a start up company based in Ohio. The logo is attached. We are a healthcare company. We are open to all designs but want something professional but fun; creative, not boring

Industry/Entity Type

Healthcare

```html
<!DOCTYPE html>
<html lang="en">
<head>
<meta charset="utf-8">
<title>Meridian Care Link — Business Cards</title>
<link rel="stylesheet" href="https://fonts.googleapis.com/css2?family=Libre+Baskerville:wght@700&family=Questrial&display=swap">
<style>
  :root {
    --stage: #e9e7ec;
    --purple-deep: #33104f;
    --purple: #4a1a72;
    --purple-soft: rgba(255, 255, 255, 0.08);
    --green: #8cc63f;
    --blue: #4fb8db;
    --band-purple: #5e5696;
    --navy: #2b2860;
    --ink-grey: #6d6a78;
    --card-white: #f7f7f8;
  }
  * { box-sizing: border-box; margin: 0; padding: 0; }
  html, body { width: 1200px; height: 800px; overflow: hidden; }
  body {
    background: var(--stage);
    font-family: "Questrial", "Century Gothic", sans-serif;
    display: flex;
    align-items: center;
    justify-content: center;
    gap: 40px;
  }
  .card {
    position: relative;
    width: 530px;
    height: 302px;
    border-radius: 4px;
    overflow: hidden;
    box-shadow: 0 10px 30px rgba(40, 20, 60, 0.18);
  }

  /* Front */
  .card--front {
    background: radial-gradient(circle at 40% 35%, var(--purple) 0%, var(--purple-deep) 80%);
    color: #fff;
  }
  .front-decor { position: absolute; inset: 0; }
  .front-mark {
    position: absolute;
    left: 0; right: 0; top: 96px;
    display: flex;
    align-items: center;
    justify-content: center;
    gap: 14px;
  }
  .front-mark__dot {
    width: 40px; height: 40px;
    border-radius: 50%;
    background: var(--green);
  }
  .front-mark__name {
    font-family: "Libre Baskerville", Georgia, serif;
    font-weight: 700;
    font-size: 24px;
    color: #fff;
  }
  .front-url {
    position: absolute;
    left: 0; right: 0; top: 170px;
    text-align: center;
    font-size: 11px;
    letter-spacing: 0.32em;
    color: rgba(255, 255, 255, 0.8);
  }

  /* Back */
  .card--back { background: var(--card-white); color: var(--navy); }
  .brand {
    position: absolute;
    left: 30px; top: 40px;
    display: flex;
    align-items: center;
    gap: 12px;
  }
  .brand__dot {
    width: 34px; height: 34px;
    border-radius: 50%;
    background: var(--green);
  }
  .brand__name {
    font-family: "Libre Baskerville", Georgia, serif;
    font-weight: 700;
    font-size: 21px;
    color: var(--navy);
  }
  .person {
    position: absolute;
    right: 30px; top: 132px;
    text-align: right;
  }
  .person__name { font-size: 17px; color: var(--navy); }
  .divider {
    position: absolute;
    left: 30px; right: 30px; top: 160px;
    height: 1.5px;
    background: var(--navy);
  }
  .person__title {
    position: absolute;
    right: 30px; top: 165px;
    font-size: 12px;
    color: var(--blue);
  }
  .contact {
    position: absolute;
    left: 30px; top: 196px;
    list-style: none;
    font-size: 13px;
    line-height: 1.45;
    color: var(--ink-grey);
  }
  .contact__web { color: var(--blue); }
  .contact__web b { font-weight: normal; color: var(--ink-grey); }
  .band {
    position: absolute;
    left: 0; right: 0; bottom: 0;
    height: 14px;
    display: flex;
  }
  .band__part { flex: 1; }
  .band__part--purple { background: var(--band-purple); }
  .band__part--green { background: var(--green); }
  .band__part--blue { background: var(--blue); }
</style>
</head>
<body>

  <section class="card card--front" aria-label="Card front">
    <svg class="front-decor" width="530" height="302" viewBox="0 0 530 302" aria-hidden="true">
      <circle cx="300" cy="140" r="170" fill="none" stroke="rgba(255,255,255,0.07)" stroke-width="34"/>
      <circle cx="120" cy="260" r="90" fill="rgba(255,255,255,0.05)"/>
    </svg>
    <div class="front-mark">
      <span class="front-mark__dot"></span>
      <span class="front-mark__name">Meridian Care Link</span>
    </div>
    <p class="front-url">WWW.MERIDIANCARE.COM</p>
  </section>

  <section class="card card--back" aria-label="Card back">
    <div class="brand">
      <span class="brand__dot"></span>
      <span class="brand__name">Meridian Care Link</span>
    </div>
    <div class="person">
      <p class="person__name">Rafael Okonkwo</p>
    </div>
    <div class="divider"></div>
    <p class="person__title">Director</p>
    <ul class="contact">
      <li>(+1) 614 555 0142</li>
      <li>hello@meridiancare.com</li>
      <li class="contact__web"><b>www.</b>meridiancare<b>.com</b></li>
    </ul>
    <div class="band">
      <span class="band__part band__part--purple"></span>
      <span class="band__part band__part--green"></span>
      <span class="band__part band__part--blue"></span>
    </div>
  </section>

</body>
</html>
```